Post Lockdown Ortho Special

We are running a special for (Ortho) Braces/Clear Aligner (Quorventa), till July 31st 2020. Up to $2,000 off with free Consultation and Xrays.

We need a ad to run in different formats.

Maybe something with: what better time to get braces when you have to wear a mask all the time.

Trying to rebuild our business and get people in for free consultations.

```html
<!DOCTYPE html>
<html lang="en">
<head>
<meta charset="utf-8">
<title>Post Lockdown Ortho Special</title>
<link rel="stylesheet" href="https://fonts.googleapis.com/css2?family=Arimo:wght@400;700&display=swap">
<style>
  :root {
    --brand-purple: #6a4696;
    --deep-purple: #5b3a8c;
    --leaf-green: #8dc63f;
    --mist: #eef1f6;
    --white: #ffffff;
  }
  * { box-sizing: border-box; margin: 0; padding: 0; }
  html, body {
    width: 1200px;
    height: 1200px;
    overflow: hidden;
    background: var(--brand-purple);
    font-family: "Arimo", Arial, sans-serif;
  }
  .ad-card {
    position: absolute;
    left: 0;
    top: 109px;
    width: 1200px;
    height: 982px;
    overflow: hidden;
    background: var(--mist);
  }
  .photo-area {
    position: absolute;
    inset: 0;
    background:
      radial-gradient(ellipse 32% 45% at 80% 48%, #e9c9a4 0%, rgba(233,201,164,0.55) 45%, rgba(233,201,164,0) 75%),
      radial-gradient(ellipse 22% 40% at 93% 58%, #e4c27e 0%, rgba(228,194,126,0) 80%),
      linear-gradient(100deg, #f4f6fa 0%, #e6ebf3 40%, #eef0f4 60%, #f2ede6 100%);
  }
  .frame-shapes {
    position: absolute;
    inset: 0;
    width: 100%;
    height: 100%;
  }
  .practice-name {
    position: absolute;
    left: 157px;
    top: 352px;
    display: flex;
    align-items: center;
    gap: 22px;
    color: var(--deep-purple);
    font-weight: 700;
  }
  .practice-name .mark-dot {
    width: 88px;
    height: 88px;
    border-radius: 50%;
    background: var(--deep-purple);
  }
  .practice-name .name { font-size: 38px; line-height: 1.1; }
  .practice-name .doctor { font-size: 19px; line-height: 1.4; display: block; }
  .offer {
    position: absolute;
    left: 60px;
    top: 560px;
    width: 730px;
    text-align: center;
    color: var(--brand-purple);
  }
  .offer .intro { font-size: 27px; font-weight: 400; line-height: 1.5; }
  .offer .deal { font-size: 35px; font-weight: 700; line-height: 1.4; }
  .mask-line {
    position: absolute;
    left: 166px;
    top: 922px;
  }
  .tagline-pill {
    position: absolute;
    left: 166px;
    top: 731px;
    width: 588px;
    height: 98px;
    border-radius: 18px;
    background: var(--leaf-green);
    color: var(--white);
    font-weight: 700;
    font-size: 24px;
    line-height: 1.35;
    text-transform: uppercase;
    display: flex;
    align-items: center;
    justify-content: center;
    text-align: center;
    padding: 0 20px;
  }
</style>
</head>
<body>
  <main class="ad-card">
    <div class="photo-area" role="img" aria-label="Photograph of a dentist in safety glasses and a lowered face mask working in a bright clinic"></div>

    <svg class="frame-shapes" viewBox="0 0 880 720" preserveAspectRatio="none" aria-hidden="true">
      <path class="top-band" fill="#6a4696" fill-opacity="0.9"
        d="M0,0 H880 V60 C820,50 770,80 720,130 C680,170 620,175 575,140 C530,100 480,70 410,72 C260,80 110,160 0,235 Z"/>
      <path class="top-swoosh" fill="#8dc63f"
        d="M0,312 C120,190 300,95 490,98 C330,92 150,170 0,282 Z"/>
      <path class="bottom-band" fill="#6a4696"
        d="M320,720 C420,700 470,640 560,628 C650,618 720,640 880,612 V720 Z"/>
      <path class="bottom-swoosh" fill="#8dc63f"
        d="M600,680 C720,690 820,640 880,520 V560 C820,660 720,700 600,680 Z"/>
      <rect class="right-rule" x="857" y="90" width="6" height="470" fill="#8dc63f"/>
      <rect class="left-rule" x="15" y="300" width="6" height="406" fill="#8dc63f"/>
      <rect class="base-rule" x="15" y="700" width="305" height="6" fill="#8dc63f"/>
    </svg>

    <div class="practice-name">
      <span class="mark-dot"></span>
      <span class="name">Pinecrest Family Dentistry<span class="doctor">Dr Marissa Holloway</span></span>
    </div>

    <section class="offer">
      <p class="intro">We offer services for Braces/Clear Aligner (Quorventa),</p>
      <p class="deal">till July 31st 2020. Up to $2,000 off<br>with free Consultation and Xrays.</p>
    </section>

    <p class="tagline-pill">Better time to get braces when you<br>have to wear a mask all the time.</p>
  </main>
</body>
</html>
```